NEED BILLBOARDS FOR VELMORANCIA

we need to redo our billboards for our business. we want to have catchy, great billboards that follow standard billboard design rules. we do breast and body cosmetic surgery in Bakersfield, fresno, and stockton ca. see attached for some tips. i would like something creative, but conservative, but funny. we also won finest around 18 years in a row and can give you the logo

Target Market(s)

females 21-45

Industry/Entity Type

plastic surgery of the breast and body

Font styles to use
Serif

Requirements
Nice to have
• funny, catchy
Should not have
• pictures of women that are overly exposed

```html
<!DOCTYPE html>
<html lang="en">
<head>
<meta charset="utf-8">
<title>Velmorancia Billboard</title>
<link rel="stylesheet" href="https://fonts.googleapis.com/css2?family=Didact+Gothic&family=Montserrat:wght@500;600;800&display=swap">
<style>
  :root {
    --stage: #7d7d7d;
    --green: #89cd8c;
    --pink: #fda4c1;
    --pink-soft: #fde9f2;
    --pink-text: #d4738f;
    --rose-text: #d96f8c;
    --white: #ffffff;
    --skin-light: #e8b08c;
    --skin-dark: #b86e46;
  }
  * { box-sizing: border-box; margin: 0; padding: 0; }
  html, body { width: 1072px; height: 1200px; overflow: hidden; }
  body {
    background: var(--stage);
    position: relative;
    font-family: "Montserrat", sans-serif;
  }
  .billboard {
    position: absolute;
    left: 36px; top: 404px;
    width: 1000px; height: 392px;
    background: linear-gradient(to bottom, var(--white) 0 161px, var(--pink-soft) 161px);
    overflow: hidden;
  }
  .corner-shape { position: absolute; left: 0; top: 0; }
  .brand {
    position: absolute;
    left: 355px; top: 48px;
    width: 380px;
    text-align: center;
  }
  .brand-name {
    font-family: "Didact Gothic", sans-serif;
    font-size: 60px;
    line-height: 1;
    color: var(--green);
    letter-spacing: -1px;
    display: flex; align-items: center; justify-content: center; gap: 10px;
  }
  .brand-dot { width: 14px; height: 14px; border-radius: 50%; background: var(--pink); }
  .brand-tagline {
    font-family: "Didact Gothic", sans-serif;
    font-size: 13px;
    color: var(--pink-text);
    margin-top: 6px;
    letter-spacing: 0.2px;
  }
  .services {
    position: absolute;
    left: 241px; top: 161px;
    width: 759px; height: 89px;
    background: var(--pink);
    display: flex; align-items: center;
    padding-left: 45px;
  }
  .service {
    width: 178px;
    text-align: center;
    color: var(--white);
    font-weight: 800;
    font-size: 18px;
    line-height: 1.25;
  }
  .service + .service { border-left: 2px solid var(--white); }
  .award {
    position: absolute;
    left: 294px; top: 273px;
    display: flex; align-items: center; gap: 6px;
    color: var(--rose-text);
    font-weight: 500; font-size: 23px;
  }
  .award-badge { width: 50px; height: 50px; border-radius: 50%; background: #2f4f9a; }
  .contact {
    position: absolute;
    left: 288px; top: 333px;
    width: 483px; height: 36px;
    border-radius: 18px;
    display: flex; overflow: hidden;
    border: 2px solid var(--white);
  }
  .contact-item {
    display: flex; align-items: center; gap: 12px;
    color: var(--white);
    font-weight: 600; font-size: 18px;
    padding-left: 12px;
  }
  .contact-phone { background: var(--pink); width: 205px; }
  .contact-web { background: var(--green); flex: 1; padding-left: 14px; gap: 22px; border-radius: 18px 0 0 18px; margin-left: -10px; }
  .contact-icon {
    width: 24px; height: 24px; border-radius: 50%;
    background: var(--white);
    display: flex; align-items: center; justify-content: center;
  }
  .model-photo {
    position: absolute;
    left: 776px; top: 0;
    width: 224px; height: 392px;
    background: radial-gradient(ellipse 40% 55% at 50% 50%, var(--skin-light), var(--skin-dark) 70%, transparent 72%);
  }
</style>
</head>
<body>
  <section class="billboard">
    <svg class="corner-shape" width="420" height="300" viewBox="0 0 420 300" aria-hidden="true">
      <path d="M0 0 H300 C220 60 230 170 130 230 C80 262 30 280 0 298 Z" fill="var(--green)"/>
    </svg>

    <div class="brand">
      <div class="brand-name">Velmorancia<span class="brand-dot"></span></div>
      <div class="brand-tagline">COSMETIC SURGERY AND MEDICAL AESTHETICS</div>
    </div>

    <div class="services">
      <div class="service">BREAST<br>PROCEDURES</div>
      <div class="service">FACIAL<br>PROCEDURES</div>
      <div class="service">BODY<br>PROCEDURES</div>
    </div>

    <div class="award">
      <span class="award-badge"></span>
      <span>Won finest around 18 years in a row</span>
    </div>

    <div class="contact">
      <div class="contact-item contact-phone">
        <span class="contact-icon">
          <svg width="14" height="14" viewBox="0 0 24 24" aria-hidden="true"><path d="M6.6 10.8a15 15 0 0 0 6.6 6.6l2.2-2.2c.3-.3.7-.4 1-.2 1.1.4 2.3.6 3.6.6.6 0 1 .4 1 1V20c0 .6-.4 1-1 1A17 17 0 0 1 3 4c0-.6.4-1 1-1h3.5c.6 0 1 .4 1 1 0 1.3.2 2.5.6 3.6.1.3 0 .7-.2 1z" fill="var(--pink)"/></svg>
        </span>
        <span>(555) 014-2290</span>
      </div>
      <div class="contact-item contact-web">
        <span class="contact-icon">
          <svg width="14" height="14" viewBox="0 0 24 24" aria-hidden="true" fill="none" stroke="var(--green)" stroke-width="2"><circle cx="12" cy="12" r="9"/><path d="M3 12h18M12 3c3 3 3 15 0 18M12 3c-3 3-3 15 0 18"/></svg>
        </span>
        <span>www.velmorancia.com</span>
      </div>
    </div>

    <div class="model-photo" role="img" aria-label="Photo of a fit woman's torso in white sportswear"></div>
  </section>
</body>
</html>
```